Business Card for Academic Coach

I need a business card designed for me - a private tutor/academic coach.

Glen Mabery
Academic Coach
AB Pellwood University, 1994 Cum Laude
Phone: 404-555-0187
glenrmabery@tutormail-example.com

Subjects
QET and BRT
Math, Physics, Writing

```html
<!DOCTYPE html>
<html lang="en">
<head>
<meta charset="utf-8">
<title>Glen Mabery – Academic Coach Business Card</title>
<link rel="stylesheet" href="https://fonts.googleapis.com/css2?family=Great+Vibes&family=Lato:wght@400;700&display=swap">
<style>
  :root {
    --page-bg: #d9d9d9;
    --card-black: #0b0b0b;
    --pattern-dark: #111111;
    --pattern-light: #1e1e1e;
    --ink-white: #ffffff;
    --ink-soft: #f2f2f2;
  }
  html, body {
    margin: 0;
    padding: 0;
    width: 1200px;
    height: 1000px;
    overflow: hidden;
    background: var(--page-bg);
  }
  .canvas {
    position: relative;
    width: 1200px;
    height: 1000px;
  }
  .card {
    position: absolute;
    width: 700px;
    height: 400px;
    background: var(--card-black);
    overflow: hidden;
    box-shadow: 0 6px 18px rgba(0,0,0,0.25);
  }
  .card-front { left: 90px; top: 70px; }
  .card-back { left: 410px; top: 530px; }
  .formula-texture {
    position: absolute;
    inset: 0;
    background: radial-gradient(ellipse at 50% 50%, var(--pattern-light) 0%, var(--pattern-dark) 60%, var(--card-black) 100%);
  }
  .front-content {
    position: absolute;
    inset: 0;
    display: flex;
    flex-direction: column;
    align-items: center;
    justify-content: center;
    color: var(--ink-white);
    text-align: center;
  }
  .name-script {
    font-family: "Great Vibes", cursive;
    font-size: 124px;
    line-height: 1;
    margin: 0 0 18px;
    font-weight: 400;
  }
  .subjects-label,
  .subjects-list {
    font-family: "Lato", sans-serif;
    font-size: 22px;
    color: var(--ink-soft);
    margin: 0;
    line-height: 1.35;
  }
  .back-content {
    position: absolute;
    right: 44px;
    bottom: 40px;
    text-align: right;
    font-family: "Lato", sans-serif;
    color: var(--ink-soft);
  }
  .contact-name {
    font-weight: 700;
    font-size: 28px;
    color: var(--ink-white);
    margin: 0 0 4px;
    letter-spacing: 0.5px;
  }
  .contact-line {
    font-size: 21px;
    margin: 0;
    line-height: 1.42;
  }
</style>
</head>
<body>
<main class="canvas">
  <section class="card card-front">
    <div class="formula-texture" role="img" aria-label="Faint handwritten physics and maths formulas covering the card background"></div>
    <div class="front-content">
      <h1 class="name-script">Glen Mabery</h1>
      <p class="subjects-label">Subjects:</p>
      <p class="subjects-list">QET and BRT, Mathematics, Physics and Writing.</p>
    </div>
  </section>

  <section class="card card-back">
    <div class="formula-texture" role="img" aria-label="Faint handwritten physics and maths formulas, including a large E = mc², covering the card background"></div>
    <div class="back-content">
      <p class="contact-name">GLEN MABERY</p>
      <p class="contact-line">Academic Coach</p>
      <p class="contact-line">AB Pellwood University, 1994 Cum Laude</p>
      <p class="contact-line">Phone: 404-555-0187</p>
      <p class="contact-line">Email: glenrmabery@tutormail-example.com</p>
    </div>
  </section>
</main>
</body>
</html>
```